Hi Performance Vehicle Import business needs a Business card

Kestrelwick Is a Melbourne based company importing and complying Japanese,American and European vehicles. We are expanding our company to a bigger factory in hopes to also expand our client base.

currently on our business cards we are advertising for the following
-Japanese, American and European vehicle importers
-ADR Compliance
-Direct import solutions
-Vehicle sales
-General maintenance

What we would like, is for customers to understand what we specialize in and be able to communicate with them by just looking at our business card.

We also have attached our current logo and previous cards with look outdated at the moment.

Target Market(s)

We are specializing in special enthusiast vehicles and only target a niche market as Imports in Australia are not very popular so we need to get our massage to everyone whos out there interested in such vehicles. We currently import Torvana Wavecrest Rtx's, Hokarimo Vex, Brant Outrunners, Velloria's , Pell Coursers, Tivano's and Lugeno and Quirt's near future.We are targeting younger generation as well as mature crowd bit of everyone..

Industry/Entity Type

Advertising

Requirements
Must have
• Lets look at few designs and we will work with the designer once preferable design has been selected.
Nice to have
• We would like to see something in the back ground to represent the automotive field. Bring your creativity so we might change our mind. We still like to keep the existing logo.
Should not have
• The business cards attached are from our local designer. We think they are outdated,wrong fonts and arrangement of the information is not quite right. So we would like to see something totally different.

```html
<!DOCTYPE html>
<html lang="en">
<head>
<meta charset="utf-8">
<title>Kestrelwick Business Card</title>
<link rel="stylesheet" href="https://fonts.googleapis.com/css2?family=Open+Sans:wght@400;600;700&display=swap">
<style>
  :root {
    --page-bg: #e9e9ea;
    --card-top: #3d3d3f;
    --card-bottom: #29292b;
    --text-main: #ffffff;
    --text-soft: #e4e4e4;
    --brand-red: #c8202a;
    --car-dark: #1c1c1e;
    --car-mid: #343437;
    --floor-red: #7a2a2e;
    --floor-dark: #2b2b2d;
  }
  html, body {
    margin: 0;
    width: 1200px;
    height: 1000px;
    overflow: hidden;
    background: var(--page-bg);
    font-family: "Open Sans", Arial, sans-serif;
  }
  .business-card {
    position: absolute;
    left: 100px;
    top: 200px;
    width: 1000px;
    height: 600px;
    background: linear-gradient(170deg, var(--card-top), var(--card-bottom));
    box-shadow: 0 10px 30px rgba(0,0,0,0.25);
    overflow: hidden;
    color: var(--text-main);
  }
  .car-photo {
    position: absolute;
    left: 224px;
    top: 100px;
    width: 776px;
    height: 380px;
    background: radial-gradient(ellipse at 70% 50%, var(--car-mid) 0%, var(--car-dark) 55%, rgba(41,41,43,0) 80%);
    opacity: 0.85;
  }
  .showroom-floor {
    position: absolute;
    left: 560px;
    top: 440px;
    width: 440px;
    height: 160px;
    background: linear-gradient(160deg, rgba(43,43,45,0) 0%, var(--floor-red) 55%, var(--floor-dark) 100%);
    opacity: 0.7;
  }
  .brand-block {
    position: absolute;
    left: 40px;
    top: 40px;
  }
  .brand-name {
    display: flex;
    align-items: center;
    gap: 14px;
    font-size: 60px;
    font-weight: 700;
    letter-spacing: 2px;
    color: var(--text-main);
    line-height: 1;
  }
  .brand-mark {
    width: 34px;
    height: 34px;
    border-radius: 50%;
    background: var(--brand-red);
  }
  .brand-meta {
    display: flex;
    justify-content: space-between;
    width: 590px;
    margin-top: 14px;
    font-size: 10px;
    font-weight: 700;
    letter-spacing: 0.5px;
    text-transform: uppercase;
    color: var(--text-soft);
  }
  .person {
    position: absolute;
    left: 40px;
    top: 268px;
  }
  .person-name {
    font-size: 27px;
    font-weight: 700;
    margin: 0;
    line-height: 1.3;
    text-transform: uppercase;
  }
  .person-title {
    font-size: 27px;
    margin: 0;
    color: var(--text-soft);
    line-height: 1.3;
  }
  .contact-list {
    position: absolute;
    left: 40px;
    top: 372px;
    margin: 0;
    padding: 0;
    list-style: none;
    font-size: 26px;
    line-height: 1;
  }
  .contact-list li {
    display: flex;
    align-items: center;
    gap: 18px;
    height: 45px;
  }
  .contact-icon {
    width: 34px;
    height: 30px;
    flex: none;
  }
  .web-links {
    position: absolute;
    right: 36px;
    top: 396px;
    text-align: right;
    font-size: 27px;
    line-height: 1;
  }
  .web-links p { margin: 0 0 16px; display: flex; justify-content: flex-end; align-items: center; gap: 6px; }
  .social-square {
    width: 38px;
    height: 38px;
    background: #3b5a98;
    border-radius: 3px;
  }
  .address {
    position: absolute;
    left: 0;
    right: 0;
    top: 528px;
    text-align: center;
    font-size: 27px;
    padding-left: 90px;
  }
</style>
</head>
<body>
  <section class="business-card">
    <div class="car-photo" role="img" aria-label="Dark photo of a black sports car in a showroom"></div>
    <div class="showroom-floor" role="img" aria-label="Red and dark chequered showroom floor"></div>

    <div class="brand-block">
      <div class="brand-name"><span class="brand-mark"></span>KESTRELWICK</div>
      <div class="brand-meta">
        <span>High Performance Vehicle Importers</span>
        <span>kestrelwick.com.au</span>
      </div>
    </div>

    <div class="person">
      <h1 class="person-name">Dalen Marsh</h1>
      <p class="person-title">Managing Director</p>
    </div>

    <ul class="contact-list">
      <li>
        <svg class="contact-icon" viewBox="0 0 34 30"><rect x="1" y="1" width="32" height="28" fill="#fff"/><path d="M10 7c-2 1-3 3-2 6 2 5 6 9 11 11 3 1 5 0 6-2l-4-4-3 2c-2-1-4-3-5-5l2-3z" fill="#222"/></svg>
        <span>(+61) 0400 555 018</span>
      </li>
      <li>
        <svg class="contact-icon" viewBox="0 0 34 30"><rect x="1" y="1" width="32" height="28" fill="#fff"/><rect x="9" y="5" width="16" height="8" fill="#222"/><rect x="6" y="14" width="22" height="11" fill="#222"/><rect x="10" y="17" width="14" height="2" fill="#fff"/><rect x="10" y="21" width="14" height="2" fill="#fff"/></svg>
        <span>(+61) 03 9000 4417</span>
      </li>
      <li>
        <svg class="contact-icon" viewBox="0 0 34 30"><rect x="1" y="1" width="32" height="28" fill="#fff"/><rect x="6" y="8" width="22" height="15" fill="none" stroke="#222" stroke-width="2"/><path d="M6 8l11 9 11-9" fill="none" stroke="#222" stroke-width="2"/></svg>
        <span>sales@Kestrelwick.com.au</span>
      </li>
    </ul>

    <div class="web-links">
      <p>Visit Kestrelwick.com.au</p>
      <p><span class="social-square"></span>/Kestrelwick.com.au</p>
    </div>

    <p class="address">Unit 4/88 Harrowgate Road Brenfield Vic 3999</p>
  </section>
</body>
</html>
```